VCS Brochure similar to Phone Brochure.

I'd like a brochure that looks good alongside the Phone services brochure, but this time offers description for Veltrix Cloud Systems instead of Phones.

Ideally, the brochure will use a front page that is very similar to the phone brochure so that they look nice together. Under who we are, we could change the "70% renewable..." to "Established in 2004" (I need to check that year). But really, just changing the two pages with the titles "Video Conferencing Room Configuration" and "IP Video Telephony". And the picture on the back page under our partner's logo.

I'll have to find more information specifically for the VCS section, but pictures can figure prominently as they did in your original brochure.

I will also want another brochure talking about Brindle Office Suite and Quorvane Office 880 which will follow this in another contest later.

There are basically 2 sides that are going to see major text changes from the phone brochures.

1) "Cloud Phone Service" would become "VCS Assessment and Migration"
-Business continuity and disaster recovery
-Security and compliance planning
-Server and data migration
-Proof of concept
-License management
-Financial assessment and optimization
-Education and training
-Readiness assessment
-VCS cost estimation
-Hybrid backup solution for networks
-Integrate with your existing infrastructure

2) "Cloud Video Telephony" would become "VCS Implementation and Maintenance"
-Backups and business continuity
-Hybrid network interoperability
-Scalability ad growth planning
-High-performance computing clusters
-Billing and cost management
-Virtual private networks in the cloud
-Desktop application offloading
-Legacy application integration
-Infrastructure resiliency
-Global network and workload optimization

Target Market(s)

Small/Medium Businesses

Requirements
Must have
• Match nicely with the Phone brochure from an earlier contest. I've attached it to this Briefing.

```html
<!DOCTYPE html>
<html lang="en">
<head>
<meta charset="utf-8">
<title>Northwave Consulting – VCS Brochure</title>
<link rel="stylesheet" href="https://fonts.googleapis.com/css2?family=Lato:wght@300;400;700;900&display=swap">
<style>
:root{
  --bg:#c4c4c6;
  --blue:#0a78c0;
  --blue-light:#1aa0e0;
  --blue-dark:#064a7a;
  --navy:#063556;
  --grey-tab:#555d66;
  --text:#1c1c1c;
  --white:#ffffff;
  --paper:#f4f4f4;
}
*{margin:0;padding:0;box-sizing:border-box}
html,body{width:879px;height:1200px;overflow:hidden;background:var(--bg);font-family:'Lato',sans-serif;color:var(--text)}
.sheet{position:absolute;left:53px;width:774px;height:552px;overflow:hidden;background:var(--white)}
.sheet-outside{top:28px}
.sheet-inside{top:597px}
.sheet svg.shapes{position:absolute;left:0;top:0}
.abs{position:absolute}
.tab{position:absolute;background:var(--grey-tab);color:var(--white);font-size:11.5px;font-weight:400;letter-spacing:.1px;padding:0 8px;height:20px;line-height:20px;white-space:nowrap;border-radius:0 4px 4px 0;box-shadow:2px 2px 0 #2f353b}
.ticks{position:absolute;list-style:none;font-size:10px;line-height:16.5px;white-space:nowrap}
.ticks li{position:relative;padding-left:15px}
.ticks li::before{content:"";position:absolute;left:0;top:4px;width:8px;height:8px;border:1.5px solid var(--blue);border-radius:50%}
.ticks li::after{content:"";position:absolute;left:3px;top:5px;width:5px;height:3px;border-left:1.6px solid var(--navy);border-bottom:1.6px solid var(--navy);transform:rotate(-45deg)}
.ticks.roomy{line-height:21.6px}
.ticks.roomy li::before{top:6.5px}
.ticks.roomy li::after{top:7.5px}
.about-title{left:17px;top:164px;color:var(--blue);font-size:20px;font-weight:300;line-height:22px}
.about-title b{display:block;font-weight:700}
.about-rule{left:17px;top:212px;width:36px;height:3px;background:var(--blue)}
.partners{left:16px;top:411px;width:236px;height:94px;border:1.5px solid var(--blue);border-radius:8px;background:var(--white)}
.partners-pill{left:68px;top:-11px;width:100px;height:19px;line-height:19px;text-align:center;background:var(--blue);color:var(--white);font-size:11px;font-weight:700;border-radius:10px}
.badge{position:absolute;border-radius:3px}
.footer-band{position:absolute;top:517px;height:27px;line-height:27px;font-size:12px;text-align:center;white-space:nowrap}
.brand{position:absolute;text-align:center;font-weight:700;letter-spacing:.5px;white-space:nowrap}
.brand .mark{display:inline-block;width:22px;height:22px;border-radius:50%;vertical-align:middle;margin-right:6px}
.contact{position:absolute;left:258px;width:258px;text-align:center;color:var(--white);font-size:10.5px;white-space:nowrap}
.contact-title{font-weight:700;font-size:11.5px}
.services-title{left:275px;top:14px;color:var(--white);font-size:20px;font-weight:300;line-height:21px}
.services-title b{display:block;font-weight:700}
.service-label{position:absolute;width:90px;margin-left:-45px;text-align:center;color:#cfe8f8;font-size:10px;line-height:11px;white-space:nowrap}
</style>
</head>
<body>

<section class="sheet sheet-outside">
  <svg class="shapes" width="774" height="552" viewBox="0 0 774 552">
    <defs>
      <linearGradient id="paperGrad" x1="0" y1="0" x2="1" y2="0">
        <stop offset="0" stop-color="#ffffff"/><stop offset="1" stop-color="#dcdcdc"/>
      </linearGradient>
      <linearGradient id="blueGrad" x1="0" y1="0" x2="0" y2="1">
        <stop offset="0" stop-color="#0b5f97"/><stop offset=".5" stop-color="#0e7cc0"/><stop offset="1" stop-color="#0a5688"/>
      </linearGradient>
      <radialGradient id="techGrad" cx=".5" cy=".5" r=".6">
        <stop offset="0" stop-color="#5a8fb8"/><stop offset=".6" stop-color="#1e4f78"/><stop offset="1" stop-color="#0c2d4a"/>
      </radialGradient>
      <linearGradient id="crowdGrad" x1="0" y1="0" x2="0" y2="1">
        <stop offset="0" stop-color="#9aa4b0"/><stop offset=".6" stop-color="#6c7785"/><stop offset="1" stop-color="#d9dde2"/>
      </linearGradient>
      <radialGradient id="caseGrad" cx=".5" cy=".5" r=".5">
        <stop offset="0" stop-color="#f6f6f6"/><stop offset="1" stop-color="#c9d3dc"/>
      </radialGradient>
      <clipPath id="clipTech"><rect x="430" y="0" width="344" height="552"/></clipPath>
    </defs>
    <rect x="0" y="0" width="258" height="552" fill="url(#paperGrad)"/>
    <rect x="258" y="0" width="258" height="552" fill="url(#blueGrad)"/>
    <rect x="516" y="0" width="258" height="552" fill="#ffffff"/>
    <path d="M0 0 H290 C250 85 170 140 60 140 C35 140 15 136 0 130 Z" fill="url(#crowdGrad)" role="img" aria-label="Photo: crowd of business silhouettes facing a glowing globe of media screens"/>
    <path d="M0 130 C20 142 45 148 70 148 C180 148 258 90 295 0" fill="none" stroke="var(--blue)" stroke-width="5"/>
    <path d="M0 140 C30 154 60 157 90 155 C190 147 262 95 305 0" fill="none" stroke="#7fc4ec" stroke-width="2"/>
    <rect x="533" y="0" width="232" height="10" rx="5" fill="var(--blue)"/>
    <g clip-path="url(#clipTech)">
      <circle cx="651" cy="404" r="214" fill="none" stroke="var(--blue)" stroke-width="7"/>
      <circle cx="651" cy="404" r="205" fill="url(#techGrad)" role="img" aria-label="Photo: businessman touching a cloud network of service icons"/>
    </g>
    <circle cx="407" cy="402" r="67" fill="#5a9fd0" opacity=".5"/>
    <circle cx="407" cy="402" r="61" fill="url(#caseGrad)" role="img" aria-label="Photo: grey rugged equipment carry case"/>
    <rect x="0" y="517" width="258" height="27" fill="var(--blue-dark)"/>
    <path d="M258 517 H460 C470 530 478 540 486 552 H258 Z" fill="#ffffff"/>
  </svg>

  <h1 class="abs about-title">ABOUT <b>NORTHWAVE</b></h1>
  <div class="abs about-rule"></div>

  <div class="tab" style="left:18px;top:232px">WHO WE ARE</div>
  <ul class="ticks" style="left:20px;top:257px">
    <li>Established in 2004</li>
    <li>100% Renewable for 2020</li>
  </ul>

  <div class="tab" style="left:18px;top:301px">WE GIVE OUR TIME AND SKILLS TO HELP</div>
  <ul class="ticks" style="left:20px;top:326px">
    <li>Schools</li>
    <li>Community Associations</li>
    <li>Non-profils</li>
    <li>Renewable Energy Initiatives</li>
  </ul>

  <div class="abs partners">
    <div class="abs partners-pill">OUR PARTNERS</div>
    <div class="badge" style="left:12px;top:24px;width:70px;height:12px;background:#6f7f90"></div>
    <div class="badge" style="left:90px;top:20px;width:60px;height:16px;background:#d7262e"></div>
    <div class="badge" style="left:165px;top:20px;width:60px;height:16px;background:#f08a1c"></div>
    <div class="badge" style="left:12px;top:56px;width:50px;height:26px;background:#8cc63f"></div>
    <div class="badge" style="left:72px;top:62px;width:44px;height:12px;background:#7a7a7a"></div>
    <div class="badge" style="left:130px;top:54px;width:30px;height:30px;border-radius:50%;background:#d2202c"></div>
    <div class="badge" style="left:180px;top:60px;width:34px;height:16px;background:#1f4e86"></div>
  </div>

  <div class="footer-band" style="left:0;width:258px;color:var(--white)">www.northwave-consult.com</div>
  <div class="footer-band" style="left:258px;width:200px;color:var(--text);font-size:12.5px">www.northwave-consult.com</div>

  <div class="brand" style="left:258px;width:258px;top:112px;color:var(--white);font-size:15px"><span class="mark" style="background:var(--white)"></span>NORTHWAVE</div>
  <div class="abs" style="left:303px;top:148px;width:168px;text-align:center;color:var(--white);font-size:8px;letter-spacing:4px;border-top:1px solid #fff;padding-top:3px">CONSULTING</div>
  <div class="contact contact-title" style="top:191px">—— CONTACT US ——</div>
  <div class="contact" style="top:216px">info@northwave-consult.com</div>
  <div class="contact" style="top:242px">
    <svg width="12" height="12" viewBox="0 0 12 12" style="vertical-align:-2px"><circle cx="6" cy="6" r="5.2" fill="none" stroke="#fff"/><path d="M4 3.2 L5 3 L5.6 4.6 L5 5.1 C5.4 6 6 6.6 6.9 7 L7.4 6.4 L9 7 L8.8 8 C6 8.4 3.6 6 4 3.2Z" fill="#fff"/></svg>
    555-014-2290</div>
  <div class="contact" style="top:270px;font-weight:700">toll free number 1-800-555-0147</div>
  <div class="contact" style="top:298px">www.northwave-consult.com</div>

  <div class="brand" style="left:516px;width:258px;top:106px;color:#3b4450;font-size:19px"><span class="mark" style="background:var(--blue-light);width:28px;height:28px"></span>NORTHWAVE</div>
  <div class="abs" style="left:545px;top:146px;width:200px;text-align:center;color:var(--blue);font-size:8.5px;letter-spacing:4px">CONSULTING</div>
  <div class="abs" style="left:516px;width:258px;top:166px;text-align:center;font-size:12px">www.northwave-consult.com</div>
</section>

<section class="sheet sheet-inside">
  <svg class="shapes" width="774" height="552" viewBox="0 0 774 552">
    <defs>
      <linearGradient id="blueGrad2" x1="0" y1="0" x2="0" y2="1">
        <stop offset="0" stop-color="#0a6fb2"/><stop offset=".5" stop-color="#0e85c8"/><stop offset="1" stop-color="#075a92"/>
      </linearGradient>
      <linearGradient id="cloudHandGrad" x1="0" y1="0" x2="1" y2="1">
        <stop offset="0" stop-color="#aab6c2"/><stop offset=".5" stop-color="#4f6680"/><stop offset="1" stop-color="#1d3550"/>
      </linearGradient>
      <linearGradient id="teamGrad" x1="0" y1="0" x2="1" y2="1">
        <stop offset="0" stop-color="#e6e0d8"/><stop offset=".6" stop-color="#b8b2aa"/><stop offset="1" stop-color="#e9eef2"/>
      </linearGradient>
      <radialGradient id="devicesGrad" cx=".5" cy=".5" r=".5">
        <stop offset="0" stop-color="#ffffff"/><stop offset="1" stop-color="#d3d7dc"/>
      </radialGradient>
      <clipPath id="clipLeft"><rect x="0" y="0" width="262" height="552"/></clipPath>
      <clipPath id="clipRight"><rect x="500" y="0" width="274" height="552"/></clipPath>
    </defs>
    <rect x="0" y="0" width="258" height="552" fill="#ffffff"/>
    <rect x="258" y="0" width="262" height="552" fill="url(#blueGrad2)"/>
    <rect x="520" y="0" width="254" height="552" fill="#ffffff"/>
    <g clip-path="url(#clipLeft)">
      <circle cx="150" cy="555" r="240" fill="none" stroke="var(--blue)" stroke-width="6"/>
      <circle cx="150" cy="555" r="232" fill="url(#cloudHandGrad)" role="img" aria-label="Photo: businessman pressing a cloud icon surrounded by device icons"/>
    </g>
    <g clip-path="url(#clipRight)">
      <path d="M500 0 H774 V205 C720 240 620 230 560 175 C520 135 505 70 500 0Z" fill="#5d6670"/>
      <path d="M510 0 H774 V196 C720 228 625 220 568 168 C532 132 516 70 510 0Z" fill="var(--blue)"/>
      <path d="M518 0 H774 V188 C720 216 630 208 575 160 C540 126 524 70 518 0Z" fill="url(#teamGrad)" role="img" aria-label="Photo: business team gathered around a laptop"/>
    </g>
    <circle cx="563" cy="167" r="48" fill="#ffffff" stroke="#dfe3e7" stroke-width="3"/>
    <circle cx="563" cy="167" r="42" fill="url(#devicesGrad)" role="img" aria-label="Photo: video conferencing screen, tablet and desk phone"/>
  </svg>

  <div class="tab" style="left:19px;top:24px">VCS ASSESSMENT AND MIGRATION</div>
  <ul class="ticks roomy" style="left:28px;top:52px">
    <li>Business continuity and disaster recovery</li>
    <li>Security and compliance planning</li>
    <li>Server and data migration</li>
    <li>Proof of concept</li>
    <li>License management</li>
    <li>Financial assessment and optimization</li>
    <li>Education and training</li>
    <li>Readiness assessment</li>
    <li>VCS cost estimation</li>
    <li>Hybrid backup solution for networks</li>
    <li>Integrate with your existing infrastructure</li>
  </ul>

  <h2 class="abs services-title">OUR <b>SERVICES</b></h2>
  <div class="abs" style="left:275px;top:61px;width:38px;height:3px;background:#cfe8f8"></div>

  <svg class="shapes" width="774" height="552" viewBox="0 0 774 552" aria-hidden="true">
    <g fill="none" stroke="#ffffff" stroke-width="2">
      <circle cx="305" cy="103" r="21"/><circle cx="390" cy="103" r="21"/><circle cx="473" cy="103" r="21"/>
      <circle cx="305" cy="198" r="21"/><circle cx="390" cy="198" r="21"/><circle cx="473" cy="198" r="21"/>
      <circle cx="305" cy="290" r="21"/><circle cx="390" cy="290" r="21"/><circle cx="473" cy="290" r="21"/>
      <circle cx="305" cy="383" r="21"/><circle cx="390" cy="383" r="21"/><circle cx="473" cy="383" r="21"/>
      <circle cx="305" cy="477" r="21"/><circle cx="390" cy="477" r="21"/><circle cx="473" cy="477" r="21"/>
    </g>
    <g fill="#ffffff" stroke="#ffffff" stroke-width="1.5">
      <circle cx="305" cy="103" r="3"/><circle cx="296" cy="94" r="2.5"/><circle cx="314" cy="94" r="2.5"/><circle cx="296" cy="112" r="2.5"/><circle cx="314" cy="112" r="2.5"/>
      <path d="M296 94 L314 112 M314 94 L296 112" fill="none"/>
      <rect x="382" y="92" width="16" height="22" rx="2" fill="none"/><rect x="385" y="95" width="10" height="5" stroke="none"/>
      <path d="M463 108 a5 5 0 0 1 3 -9 a7 7 0 0 1 13 2 a4 4 0 0 1 1 8 Z" fill="none"/>
      <rect x="296" y="188" width="18" height="20" rx="2" fill="none"/><path d="M296 195 H314 M296 201 H314" fill="none"/>
      <path d="M378 196 a17 17 0 0 1 24 0 M382 200 a11 11 0 0 1 16 0" fill="none" stroke-width="2.5"/><circle cx="390" cy="205" r="2"/>
      <rect x="463" y="189" width="20" height="16" fill="none"/><path d="M466 194 H480 M466 198 H476" fill="none"/>
      <path d="M305 279 L316 299 H294 Z" fill="none"/><path d="M305 286 V293" fill="none"/>
      <ellipse cx="390" cy="282" rx="9" ry="3.5" fill="none"/><path d="M381 282 V298 a9 3.5 0 0 0 18 0 V282 M381 290 a9 3.5 0 0 0 18 0" fill="none"/>
      <rect x="462" y="281" width="22" height="14" fill="none"/><path d="M473 295 V300 M467 300 H479" fill="none"/>
      <rect x="294" y="379" width="22" height="11" rx="2" fill="none"/><rect x="299" y="373" width="12" height="6" fill="none"/><rect x="299" y="388" width="12" height="6" fill="none"/>
      <path d="M390 372 L399 376 V384 C399 389 394 393 390 394 C386 393 381 389 381 384 V376 Z" fill="none"/><rect x="387" y="382" width="6" height="5" stroke="none"/>
      <rect x="465" y="372" width="16" height="22" rx="2" fill="none"/><path d="M468 378 H478 M468 383 H478 M468 388 H478" fill="none"/>
      <path d="M296 486 L314 468" fill="none" stroke-width="3"/><rect x="300" y="472" width="10" height="10" transform="rotate(45 305 477)" fill="none"/>
      <path d="M380 480 L400 468 L394 488 L389 482 Z" fill="none"/>
      <path d="M462 470 H484 L480 480 H466 Z" fill="none"/><circle cx="473" cy="482" r="4" fill="none"/>
    </g>
  </svg>

  <div class="service-label" style="left:305px;top:128px">Network<br>Support</div>
  <div class="service-label" style="left:390px;top:128px">Phone<br>Service</div>
  <div class="service-label" style="left:473px;top:128px">Disaster<br>Recovery</div>
  <div class="service-label" style="left:305px;top:223px">Remote<br>Backups</div>
  <div class="service-label" style="left:390px;top:223px">Wireless coverage<br>Planning</div>
  <div class="service-label" style="left:473px;top:223px">Quorvane 880<br>&amp; Brindle Apps</div>
  <div class="service-label" style="left:305px;top:314px">Spam &amp;<br>Virus Filtering</div>
  <div class="service-label" style="left:390px;top:314px">Migration<br>Services</div>
  <div class="service-label" style="left:473px;top:314px">Server &amp; Network<br>Monitoring</div>
  <div class="service-label" style="left:305px;top:408px">Printing, Scanning<br>&amp; Plotting</div>
  <div class="service-label" style="left:390px;top:408px">Firewalls<br>&amp; Security</div>
  <div class="service-label" style="left:473px;top:408px">Network Design<br>&amp; Planning</div>
  <div class="service-label" style="left:305px;top:502px">Network &amp;<br>Electrical Cabling</div>
  <div class="service-label" style="left:390px;top:502px">Email<br>Archiving</div>
  <div class="service-label" style="left:473px;top:502px">Security camera<br>&amp; Access Control</div>

  <div class="tab" style="left:528px;top:239px;font-size:10.5px;padding:0 6px">VCS IMPLEMENTATION AND MAINTENANCE</div>
  <ul class="ticks roomy" style="left:534px;top:266px">
    <li>Backups and business continuity</li>
    <li>Hybrid network interoperability</li>
    <li>Scalability ad growth planning</li>
    <li>High-performance computing clusters</li>
    <li>Billing and cost management</li>
    <li>Virtual private networks in the cloud</li>
    <li>Desktop application offloading</li>
    <li>Legacy application integration</li>
    <li>Infrastructure resiliency</li>
    <li>Global network and workload optimization</li>
  </ul>

  <div class="brand" style="left:520px;width:254px;top:485px;color:#3b4450;font-size:14px"><span class="mark" style="background:var(--blue-light)"></span>NORTHWAVE</div>
  <div class="abs" style="left:520px;width:254px;top:512px;text-align:center;color:var(--blue);font-size:7px;letter-spacing:3px">CONSULTING</div>
</section>

</body>
</html>
```